Bref créative
Limb Nestler
Naturally made in the US
Professional
Rosalind Featherstone
Owner
437 Tamsin Ave - Ste 220-581
rfeatherstone@limbnestler-example.com
Limbnestler-example.com
I'm not sure what the first two boxes refer to. I want our logo to be on the cards in the same colors.

```html
<!DOCTYPE html>
<html lang="en">
<head>
<meta charset="utf-8">
<title>Limb Nestler – Business Cards</title>
<link rel="stylesheet" href="https://fonts.googleapis.com/css2?family=Open+Sans:wght@400;600;700&display=swap">
<style>
  :root {
    --stage: #5b5b5b;
    --black: #121212;
    --white: #f4f4f4;
    --maroon: #6b1f1f;
    --blue: #2c9edb;
    --accent-red: #7a2222;
    --accent-blue: #2c9edb;
    --accent-grey: #9a9a9a;
    --ink-light: #ffffff;
    --ink-dark: #2a2a2a;
  }
  * { margin: 0; padding: 0; box-sizing: border-box; }
  html, body { width: 1200px; height: 766px; overflow: hidden; }
  body {
    background: var(--stage);
    font-family: "Open Sans", Arial, sans-serif;
    position: relative;
  }
  .card {
    position: absolute;
    width: 247px;
    height: 144px;
    border-radius: 6px;
    overflow: hidden;
    box-shadow: 0 3px 8px rgba(0,0,0,.45);
  }
  .card--black { background: var(--black); color: var(--ink-light); }
  .card--white { background: var(--white); color: var(--ink-dark); }
  .card--maroon { background: var(--maroon); color: var(--ink-light); }
  .card--blue { background: var(--blue); color: var(--ink-light); }

  .row-front { top: 240px; }
  .row-back { top: 396px; }
  .col-1 { left: 72px; }
  .col-2 { left: 331px; }
  .col-3 { left: 588px; }
  .col-4 { left: 845px; }

  .contact {
    position: absolute;
    left: 12px;
    top: 44px;
    width: 120px;
  }
  .contact__name { font-size: 8.5px; font-weight: 700; line-height: 1.1; }
  .contact__role { font-size: 5px; margin-bottom: 7px; }
  .contact__line { font-size: 4px; line-height: 1.45; white-space: nowrap; }

  .brand {
    position: absolute;
    text-align: center;
  }
  .card .brand--front { right: 10px; top: 32px; width: 106px; }
  .card .brand--back { left: 0; right: 0; top: 46px; }
  .brand__name {
    font-weight: 700;
    font-size: 15px;
    line-height: 1;
    letter-spacing: .2px;
  }
  .brand--back .brand__name { font-size: 19px; }
  .brand__tagline { font-size: 4px; margin-top: 3px; letter-spacing: .3px; }
  .brand--back .brand__tagline { font-size: 5px; }
  .card--black .brand__name { color: var(--accent-blue); }
  .card--white .brand__name { color: var(--maroon); }

  .swoosh { position: absolute; left: 0; bottom: 0; width: 247px; height: 50px; }

  .website {
    position: absolute;
    left: 0; right: 0; bottom: 10px;
    text-align: center;
    font-size: 4.5px;
  }
</style>
</head>
<body>

<!-- Front row -->
<div class="card card--black row-front col-1">
  <div class="contact">
    <p class="contact__name">Rosalind Featherstone</p>
    <p class="contact__role">Owner</p>
    <p class="contact__line">437 Tamsin Ave - Ste 220-581</p>
    <p class="contact__line">T: 555 014 2270</p>
    <p class="contact__line">C: 555 014 3381</p>
    <p class="contact__line">rfeatherstone@limbnestler-example.com</p>
  </div>
  <div class="brand brand--front">
    <p class="brand__name">limb nestler</p>
    <p class="brand__tagline">NATURALLY MADE IN THE US</p>
  </div>
  <svg class="swoosh" viewBox="0 0 247 50" preserveAspectRatio="none">
    <path d="M0 30 C70 16 150 18 247 28 L247 50 L0 50 Z" fill="var(--accent-red)"/>
    <path d="M0 36 C80 20 160 20 247 22" stroke="var(--accent-blue)" stroke-width="3" fill="none"/>
    <path d="M0 40 C90 28 170 26 247 30" stroke="var(--accent-grey)" stroke-width="1.5" fill="none"/>
  </svg>
</div>

<div class="card card--white row-front col-2">
  <div class="contact">
    <p class="contact__name">Rosalind Featherstone</p>
    <p class="contact__role">Owner</p>
    <p class="contact__line">437 Tamsin Ave - Ste 220-581</p>
    <p class="contact__line">T: 555 014 2270</p>
    <p class="contact__line">C: 555 014 3381</p>
    <p class="contact__line">rfeatherstone@limbnestler-example.com</p>
  </div>
  <div class="brand brand--front">
    <p class="brand__name">limb nestler</p>
    <p class="brand__tagline">NATURALLY MADE IN THE US</p>
  </div>
  <svg class="swoosh" viewBox="0 0 247 50" preserveAspectRatio="none">
    <path d="M0 32 C70 18 150 20 247 30 L247 50 L0 50 Z" fill="var(--accent-grey)"/>
    <path d="M0 36 C80 20 160 20 247 22" stroke="var(--accent-blue)" stroke-width="3" fill="none"/>
    <path d="M0 42 C90 28 170 28 247 34" stroke="var(--accent-red)" stroke-width="2" fill="none"/>
  </svg>
</div>

<div class="card card--maroon row-front col-3">
  <div class="contact">
    <p class="contact__name">Rosalind Featherstone</p>
    <p class="contact__role">Owner</p>
    <p class="contact__line">437 Tamsin Ave - Ste 220-581</p>
    <p class="contact__line">T: 555 014 2270</p>
    <p class="contact__line">C: 555 014 3381</p>
    <p class="contact__line">rfeatherstone@limbnestler-example.com</p>
  </div>
  <div class="brand brand--front">
    <p class="brand__name">limb nestler</p>
    <p class="brand__tagline">NATURALLY MADE IN THE US</p>
  </div>
  <svg class="swoosh" viewBox="0 0 247 50" preserveAspectRatio="none">
    <path d="M0 34 C70 20 150 22 247 32 L247 50 L0 50 Z" fill="var(--accent-grey)"/>
    <path d="M0 36 C80 20 160 20 247 22" stroke="var(--accent-blue)" stroke-width="3" fill="none"/>
    <path d="M0 42 C90 28 170 28 247 34" stroke="var(--white)" stroke-width="1.5" fill="none"/>
  </svg>
</div>

<div class="card card--blue row-front col-4">
  <div class="contact">
    <p class="contact__name">Rosalind Featherstone</p>
    <p class="contact__role">Owner</p>
    <p class="contact__line">437 Tamsin Ave - Ste 220-581</p>
    <p class="contact__line">T: 555 014 2270</p>
    <p class="contact__line">C: 555 014 3381</p>
    <p class="contact__line">rfeatherstone@limbnestler-example.com</p>
  </div>
  <div class="brand brand--front">
    <p class="brand__name">limb nestler</p>
    <p class="brand__tagline">NATURALLY MADE IN THE US</p>
  </div>
  <svg class="swoosh" viewBox="0 0 247 50" preserveAspectRatio="none">
    <path d="M0 34 C70 20 150 22 247 32 L247 50 L0 50 Z" fill="var(--accent-grey)"/>
    <path d="M0 36 C80 20 160 20 247 22" stroke="var(--white)" stroke-width="3" fill="none"/>
    <path d="M0 42 C90 28 170 28 247 34" stroke="var(--accent-red)" stroke-width="2" fill="none"/>
  </svg>
</div>

<!-- Back row -->
<div class="card card--black row-back col-1">
  <div class="brand brand--back">
    <p class="brand__name">limb nestler</p>
    <p class="brand__tagline">NATURALLY MADE IN THE US</p>
  </div>
  <p class="website">Limbnestler-example.com</p>
</div>

<div class="card card--white row-back col-2">
  <div class="brand brand--back">
    <p class="brand__name">limb nestler</p>
    <p class="brand__tagline">NATURALLY MADE IN THE US</p>
  </div>
  <p class="website">Limbnestler-example.com</p>
</div>

<div class="card card--maroon row-back col-3">
  <div class="brand brand--back">
    <p class="brand__name">limb nestler</p>
    <p class="brand__tagline">NATURALLY MADE IN THE US</p>
  </div>
  <p class="website">Limbnestler-example.com</p>
</div>

<div class="card card--blue row-back col-4">
  <div class="brand brand--back">
    <p class="brand__name">limb nestler</p>
    <p class="brand__tagline">NATURALLY MADE IN THE US</p>
  </div>
  <p class="website">Limbnestler-example.com</p>
</div>

</body>
</html>
```